Social Media Marketing Website

I would like someone to finish off my website as the previous designer has decided otherwise. I like the current layout but it can be better. I also want the site to reflect my portfolio uploaded on each brand I have worked with. I need to upload videos and make the website responsive and load very quickly. It also needs to be mobile and tablet friendly. I know my way around websites and what is current. my website is www.pkdnorthly.com

Target Market(s)

Business seeking brand consultation and ecommerce solutions

Industry/Entity Type

Digital Marketing

Coding

Coded - Design and coding required

Number of Pages Required

5+ page

Font styles to use
Other font styles liked:
• Bebas Neue

Colors
ffffff
aaaaaa
f5f5f5
fffbf0

Requirements
Must have
• Fast loading website that is easy to navigate. Can withstand video content and high res pictures. Easy backend to operate. Google Analytics Set Up.
Nice to have
• Interactive site
Should not have
• Complex design that is not easy to navigate for the non tech savvy visitor.

```html
<!DOCTYPE html>
<html lang="en">
<head>
<meta charset="utf-8">
<title>PKD Northly — Social Media Marketing</title>
<link rel="stylesheet" href="https://fonts.googleapis.com/css2?family=Oswald:wght@300;400;500;600&display=swap">
<style>
:root{
  --blue:#3385c9;
  --blue-dark:#2a74b3;
  --blue-soft:#4a94d2;
  --ink:#222;
  --text:#333;
  --grey-bg:#f0f0f0;
  --white:#ffffff;
  --footer-base:#2b2b2b;
  --muted:#8a8a8a;
}
*{box-sizing:border-box;margin:0;padding:0}
html,body{width:1200px;height:3564px;overflow:hidden}
body{font-family:"Oswald",sans-serif;color:var(--text);background:var(--white);position:relative}
.abs{position:absolute}
.btn{position:absolute;display:flex;align-items:center;justify-content:center;background:var(--blue);color:var(--white);border-radius:20px;font-size:12px;font-weight:500;letter-spacing:1px;text-transform:uppercase;box-shadow:0 3px 5px rgba(0,0,0,.18)}
.accent{color:var(--blue);font-weight:400}
.section-title{position:absolute;font-weight:300;text-transform:uppercase;color:var(--ink);letter-spacing:.5px;white-space:nowrap}
.copy{font-size:14px;font-weight:300;line-height:22px;color:var(--text)}

/* hero */
.hero{left:0;top:0;width:1200px;height:570px;background:linear-gradient(120deg,#e9e6e2 0%,#f1f0ee 45%,#e4e6e8 100%);border-bottom:4px solid #dcdcdc}
.hero-scene{left:0;top:0;width:1200px;height:566px;background:radial-gradient(ellipse at 80% 40%,rgba(200,205,210,.5),transparent 60%),radial-gradient(ellipse at 25% 55%,rgba(215,200,190,.45),transparent 55%)}
.brand{left:86px;top:12px;width:76px;height:71px;border:2px solid #555;display:flex;align-items:center;justify-content:center;text-align:center;font-size:11px;line-height:13px;color:#333;font-weight:400}
.nav{left:392px;top:38px;width:720px;display:flex;justify-content:space-between;font-size:12px;letter-spacing:.5px;color:#222}
.hero-title{left:0;width:1200px;text-align:center;color:#111;text-transform:uppercase}
.hero-copy{left:350px;top:282px;width:500px;text-align:center;font-size:14px;line-height:22px;font-weight:300;color:#333}
.dots{left:580px;top:522px;display:flex;gap:6px}
.dots span{width:6px;height:6px;border-radius:50%;background:#9bb8d3}
.dots span.on{background:var(--blue)}

/* about */
.about-visual{left:0;top:630px;width:580px;height:534px;background:linear-gradient(180deg,#1b2a3c 0%,#1f57b5 8%,#1e3fa0 60%,#1a2d6f 82%,#c9c9cb 86%,#e9e9ea 100%);border-radius:0 12px 30px 0}
.about-text{left:613px;width:500px}

/* services */
.services{left:0;top:1231px;width:1200px;height:855px;background:var(--grey-bg)}
.card{position:absolute;width:325px;height:316px;box-shadow:0 3px 6px rgba(0,0,0,.25);overflow:hidden;background:var(--blue)}
.card-art{position:absolute;left:0;top:0;width:325px;height:236px}
.card-caption{position:absolute;left:0;bottom:0;width:325px;height:80px;background:var(--blue);color:var(--white);font-size:13px;font-weight:500;line-height:22px;text-align:center;display:flex;align-items:center;justify-content:center;padding:0 40px}
.card-plain{display:flex;align-items:center;justify-content:center;color:var(--white);font-size:13px;font-weight:500;line-height:22px;text-align:center;padding:0 50px;background:linear-gradient(160deg,#3a8bd0,#2f7fc4)}
.card-all{background:#000;color:var(--white);display:flex;align-items:center;justify-content:center;font-size:18px;font-weight:500;letter-spacing:1.5px}

/* work */
.work{left:0;top:2086px;width:1200px;height:599px;background:var(--blue)}
.work-panel{left:88px;top:2210px;width:1026px;height:423px;background:var(--white);box-shadow:0 4px 10px rgba(0,0,0,.25)}
.work-head{font-size:18px;color:var(--blue);font-weight:400;margin-bottom:6px}
.work-text{font-size:11px;line-height:17px;font-weight:300;color:#444}
.work-photo{left:613px;top:2238px;width:473px;height:364px;background:radial-gradient(ellipse at 55% 45%,#5a4a40 0%,#2b2420 45%,#0c0a09 100%)}
.work-name{position:absolute;left:0;width:473px;text-align:center;color:var(--white);font-weight:300}

/* videos */
.video-visual{left:0;top:2685px;width:589px;height:340px;background:radial-gradient(circle at 50% 48%,#2a5a78 0%,#173a52 45%,#112c40 100%)}
.video-side{left:589px;top:2685px;width:611px;height:340px;background:var(--grey-bg)}

/* subscribe */
.subscribe-title{left:86px;top:3078px;font-size:36px;font-weight:300;text-transform:uppercase;color:var(--ink);white-space:nowrap}
.field{left:523px;top:3075px;width:450px;height:57px;border:1px solid #ccc;border-right:none;font-size:12px;color:#999;display:flex;align-items:center;padding-left:14px;font-weight:300;background:var(--white)}
.submit{left:955px;top:3075px;width:157px;height:57px;background:var(--blue);color:var(--white);font-size:14px;font-weight:500;display:flex;align-items:center;justify-content:center;letter-spacing:1px;border-radius:0 6px 6px 0}

/* footer */
.footer{left:0;top:3189px;width:1200px;height:318px;background:var(--blue);color:var(--white)}
.foot-head{position:absolute;top:24px;font-size:13px;font-weight:500;text-transform:uppercase;letter-spacing:.5px}
.quick{position:absolute;left:86px;top:56px;list-style:none;font-size:12px;line-height:26px;text-transform:uppercase;font-weight:400}
.post{position:absolute;left:435px;width:330px;height:60px;display:flex;gap:14px}
.post-thumb{width:59px;height:59px;flex:none}
.post-text{font-size:11px;line-height:15px;font-weight:400}
.post-text b{display:block;font-weight:600;margin-top:2px}
.contact{position:absolute;left:874px;width:238px;background:var(--blue-soft);display:flex;gap:14px;padding:12px 12px 0 16px;font-size:11px;line-height:15px}
.contact svg{flex:none;margin-top:2px}
.copyright{left:0;top:3507px;width:1200px;height:57px;background:var(--footer-base);color:var(--muted);font-size:12px;display:flex;align-items:center;justify-content:center;font-weight:300;letter-spacing:.5px}
</style>
</head>
<body>

<!-- hero -->
<section class="abs hero">
  <div class="abs hero-scene" role="img" aria-label="Faded desk scene with a laptop showing social media charts, notebooks and a coffee cup"></div>
  <div class="abs brand">PKD<br>Northly</div>
  <nav class="abs nav"><span>HOME</span><span>ABOUT</span><span>SKILLS</span><span>SERVICE</span><span>WORK</span><span>TESTIMONIAL</span><span>BLOG</span><span>TEAM</span><span>CONTACT</span></nav>
  <h1 class="abs hero-title" style="top:146px;font-size:50px;font-weight:400;letter-spacing:1px">Lorem Ipsum is</h1>
  <h2 class="abs hero-title" style="top:212px;font-size:34px;font-weight:300">Simply Dummy</h2>
  <p class="abs hero-copy">Lorem Ipsum is simply dummy text of the printing and typesetting industry. Lorem Ipsum has been the industry's standard dummy text ever since the 1500s, when an unknown printer took a galley of type and scrambled it to make a type specimen book. It has survived not only five</p>
  <div class="btn" style="left:525px;top:400px;width:147px;height:38px">Read More</div>
  <div class="abs dots"><span></span><span class="on"></span><span></span></div>
</section>

<!-- about -->
<div class="abs about-visual" role="img" aria-label="Laptop screen showing a blue social media marketing word cloud"></div>
<h2 class="section-title" style="left:613px;top:662px;font-size:40px">About <span class="accent">Our Company</span></h2>
<p class="abs copy about-text" style="top:746px">Lorem Ipsum is simply dummy text of the printing and typesetting industry. Lorem Ipsum has been the industry's standard dummy text ever since the 1500s, when an unknown printer took a galley of type and scrambled it to make a type specimen book. It has survived not only five</p>
<p class="abs copy about-text" style="top:858px">Lorem Ipsum is simply dummy text of the printing and typesetting industry. Lorem Ipsum has been the industry's standard dummy text ever since the 1500s, when an unknown printer took a galley of type.</p>
<div class="btn" style="left:613px;top:974px;width:149px;height:38px">Read More</div>

<!-- services -->
<section class="abs services"></section>
<h2 class="section-title" style="left:0;width:1200px;text-align:center;top:1278px;font-size:36px">Our <span class="accent">Service</span></h2>
<div class="card card-plain" style="left:88px;top:1373px">Lorem Ipsum is simply dummy text of the printing typesetting</div>
<div class="card" style="left:437px;top:1373px">
  <div class="card-art" role="img" aria-label="Flat illustration of charts, video player and marketing icons" style="background:linear-gradient(160deg,#3fb3c9,#2f9fbd)"></div>
  <div class="card-caption">Lorem Ipsum is simply dummy text of the printing</div>
</div>
<div class="card" style="left:789px;top:1373px">
  <div class="card-art" role="img" aria-label="Flat illustration of a megaphone over a world map and screens" style="background:linear-gradient(160deg,#2f4a66,#3c6fa3)"></div>
  <div class="card-caption">Lorem Ipsum is simply dummy text of the printing</div>
</div>
<div class="card" style="left:88px;top:1715px">
  <div class="card-art" role="img" aria-label="Phones and tablets showing responsive layouts" style="background:linear-gradient(180deg,#e9eef2,#9fc8e6)"></div>
  <div class="card-caption">Lorem Ipsum is simply dummy text of the printing</div>
</div>
<div class="card" style="left:437px;top:1715px">
  <div class="card-art" role="img" aria-label="Flat illustration of a person at a computer surrounded by cloud and social icons" style="background:linear-gradient(180deg,#f4f7fb,#d9e8f5)"></div>
  <div class="card-caption">Lorem Ipsum is simply dummy text of the printing</div>
</div>
<div class="card card-all" style="left:789px;top:1715px">VIEW ALL</div>

<!-- recent work -->
<section class="abs work"></section>
<h2 class="section-title" style="left:0;width:1200px;text-align:center;top:2133px;font-size:36px;color:var(--white)">Our <span style="font-weight:400">Recent Work</span></h2>
<div class="abs work-panel"></div>
<div class="abs" style="left:114px;top:2232px;width:476px">
  <h3 class="work-head">The Problem</h3>
  <p class="work-text">Professional Boxer Dan Corley approached PKD Northly to launch his personal-brand. Dan Corley signed as a professional to Ringside Promotions Boxing &amp; Promoter Leo Hartley.</p>
  <h3 class="work-head" style="margin-top:12px">The Solution</h3>
  <p class="work-text">PKD launched Dan Corley to the nation with a strategic plan first unveiling him to his home town at Eastmoor Athletic FC as a match day sponsor. We combined this by filming a documentary, cutting edge boxing promotional videos, photography and secured further sponsorship with our partners.<br>PKD Northly campaign tactics of mixing traditional and digital marketing has helped launch a successful boxing debut for the former Team Northland boxer. The campaign made a real lasting impact on Dan's career by selling a record number of tickets. Our promotional videos and photography sparked real conversations on digital platforms giving the brand a chance to maintain its position.</p>
</div>
<div class="btn" style="left:114px;top:2565px;width:149px;height:38px">View More</div>
<div class="abs work-photo" role="img" aria-label="Dramatic portrait of a professional boxer in gloves">
  <div class="work-name" style="top:256px;font-size:46px">Dan Corley</div>
  <div class="work-name" style="top:316px;font-size:24px">The Professional Boxer</div>
</div>

<!-- videos -->
<div class="abs video-visual" role="img" aria-label="Globe surrounded by a connected network of people">
  <svg class="abs" style="left:258px;top:154px" width="72" height="72" viewBox="0 0 72 72"><circle cx="36" cy="36" r="32" fill="rgba(255,255,255,.15)" stroke="#fff" stroke-width="4"/><path d="M29 23 L51 36 L29 49 Z" fill="#fff"/></svg>
</div>
<div class="abs video-side"></div>
<h2 class="section-title" style="left:613px;top:2738px;font-size:38px;letter-spacing:2px">Watch <span class="accent">Our Videos</span></h2>
<p class="abs copy" style="left:613px;top:2806px;width:450px">Lorem Ipsum is simply dummy text of the printing and typesetting industry. Lorem Ipsum has been the industry's standard dummy text ever since the 1500s, when an unknown printer took a galley of type and scrambled it to make a type specimen book. It has survived not only five.</p>
<div class="btn" style="left:613px;top:2923px;width:149px;height:38px">View More</div>

<!-- subscribe -->
<h2 class="abs subscribe-title">Subscribe <span class="accent">Our News Letter</span></h2>
<div class="abs field">ENTER EMAIL ID</div>
<div class="abs submit">SUBMIT</div>

<!-- footer -->
<footer class="abs footer">
  <h4 class="foot-head" style="left:86px">Quick Links</h4>
  <ul class="quick"><li>Home</li><li>About</li><li>Skills</li><li>Service</li><li>Work</li><li>Testimonial</li><li>Blog</li><li>Team</li><li>Contact</li></ul>

  <h4 class="foot-head" style="left:435px">Recent Posts</h4>
  <div class="post" style="top:54px"><div class="post-thumb" role="img" aria-label="Post thumbnail" style="background:linear-gradient(135deg,#6cc36a,#8c5bb8)"></div><div class="post-text">Lorem Ipsum is simply dummy text of the printing and typesetting industry. Lorem<b>February 20, 2015</b></div></div>
  <div class="post" style="top:133px"><div class="post-thumb" role="img" aria-label="Post thumbnail" style="background:linear-gradient(135deg,#8a6b55,#d9c4a8)"></div><div class="post-text">Lorem Ipsum is simply dummy text of the printing<b>February 20, 2015</b></div></div>
  <div class="post" style="top:211px"><div class="post-thumb" role="img" aria-label="Post thumbnail" style="background:linear-gradient(135deg,#c7d3ef,#6b7fc4)"></div><div class="post-text">Lorem Ipsum is simply dummy text of the printing andstandart<b>February 20, 2015</b></div></div>

  <h4 class="foot-head" style="left:874px">Contact Us</h4>
  <div class="contact" style="top:47px;height:67px">
    <svg width="18" height="26" viewBox="0 0 18 26"><rect x="2" y="1" width="14" height="24" rx="2" fill="none" stroke="#fff" stroke-width="1.6"/><line x1="7" y1="21" x2="11" y2="21" stroke="#fff" stroke-width="1.6"/></svg>
    <div>Phone number<br><span style="font-size:13px">+00 - 0000 - 0000</span></div>
  </div>
  <div class="contact" style="top:121px;height:69px">
    <svg width="20" height="14" viewBox="0 0 20 14"><rect x="1" y="1" width="18" height="12" fill="none" stroke="#fff" stroke-width="1.5"/><path d="M1 1 L10 8 L19 1" fill="none" stroke="#fff" stroke-width="1.5"/></svg>
    <div>Email Address</div>
  </div>
  <div class="contact" style="top:197px;height:97px">
    <svg width="18" height="20" viewBox="0 0 18 20"><path d="M17 1 L1 8 L8 10 L10 19 Z" fill="none" stroke="#fff" stroke-width="1.5" stroke-linejoin="round"/></svg>
    <div>Address<br><span style="font-size:10px;line-height:14px">Lorem Ipsum is simply dummy text of the printing and typesetting industry. Lorem</span></div>
  </div>
</footer>
<div class="abs copyright">Copyright © PKD Northly. All Rights Reserved 2016</div>

</body>
</html>
```